Brantley Advisory Group provides support for renewable energy projects to utilities and suppliers

I need a professional looking business card that is both simple and elegant and unique. My clients are mostly large organizations not individuals. I am a consultant with my own company that is small but would like to give clients the impression I am larger. Smart grid, fiber optics, software, field hardware, distribution automation, substation automation, operations, energy storage/batteries, microgrids, customer service, strategy/roadmaps, conservation, Automated Metering Infrastruture (AMI or smart meters) are all areas of focus.

Target Market(s)

Utilities, suppliers, governmental agencies involved in energy. All types of energy especially natural gas and electrical. Especially renewable energy or green projects.

Contact Information for Business Card

Name - Ross Brantley Cell Phone - 425.318.4762 Email - rbrantley@brantleyag-example.com
Company - Brantley Advisory Group (logo) Title - Principal

Font styles to use
Serif
Sans Serif

Colors

Designer to choose colors to be used in the design.

Requirements
Must have
• Simple and professional and powerful.
• Unique/creative design.
Nice to have
• Utilize color scheme to accent logo colors. Maybe some geometric pattern on edge of card with color.
Should not have
• Busy, complicated, traditional

```html
<!DOCTYPE html>
<html lang="en">
<head>
<meta charset="utf-8">
<title>Brantley Advisory Group – Business Card</title>
<link href="https://fonts.googleapis.com/css2?family=Open+Sans:wght@400;700&display=swap" rel="stylesheet">
<style>
  :root {
    --backdrop: #e9eaec;
    --brand-blue: #1f3f99;
    --brand-green: #5f9a3a;
    --text-grey: #6b6b6b;
    --paper: #ffffff;
  }
  html, body {
    margin: 0;
    width: 1200px;
    height: 913px;
    overflow: hidden;
    background: var(--backdrop);
    font-family: "Open Sans", Arial, sans-serif;
  }
  .canvas { position: relative; width: 1200px; height: 913px; }
  .card {
    position: absolute;
    width: 540px;
    height: 309px;
    border-radius: 18px;
    box-shadow: 0 6px 18px rgba(0,0,0,.18);
    overflow: hidden;
  }
  .card-front { left: 70px; top: 80px; background: var(--brand-blue); }
  .card-back { left: 590px; top: 524px; background: var(--paper); }

  .wordmark {
    display: flex;
    align-items: center;
    gap: 14px;
    font-weight: 700;
    line-height: 1.05;
  }
  .wordmark-square {
    width: 34px; height: 34px;
    border: 3px solid currentColor;
    border-radius: 4px;
    box-sizing: border-box;
    flex: none;
  }
  .wordmark-name { font-size: 30px; letter-spacing: .5px; }

  .card-front .wordmark {
    position: absolute;
    left: 50%; top: 50%;
    transform: translate(-50%, -50%);
    color: var(--paper);
    white-space: nowrap;
  }

  .card-back .wordmark {
    position: absolute;
    right: 34px; top: 34px;
    color: var(--brand-blue);
    white-space: nowrap;
  }
  .card-back .wordmark-name { font-size: 22px; }
  .card-back .wordmark-square { width: 26px; height: 26px; }

  .contact-block {
    position: absolute;
    left: 40px; bottom: 34px;
  }
  .person-name {
    margin: 0;
    font-size: 22px;
    font-weight: 700;
    color: var(--brand-blue);
    letter-spacing: .5px;
  }
  .person-title {
    margin: 0 0 14px;
    font-size: 16px;
    color: var(--text-grey);
  }
  .contact-list { list-style: none; margin: 0; padding: 0; }
  .contact-list li {
    display: flex;
    align-items: center;
    gap: 8px;
    font-size: 15px;
    color: var(--text-grey);
    line-height: 1.5;
  }
  .contact-icon { width: 13px; height: 13px; flex: none; fill: var(--brand-green); }
</style>
</head>
<body>
<main class="canvas">
  <section class="card card-front" aria-label="Card front">
    <div class="wordmark">
      <span class="wordmark-square"></span>
      <span class="wordmark-name">Brantley Advisory Group</span>
    </div>
  </section>

  <section class="card card-back" aria-label="Card back">
    <div class="wordmark">
      <span class="wordmark-square"></span>
      <span class="wordmark-name">Brantley Advisory Group</span>
    </div>
    <div class="contact-block">
      <h1 class="person-name">ROSS BRANTLEY</h1>
      <p class="person-title">Principal</p>
      <ul class="contact-list">
        <li>
          <svg class="contact-icon" viewBox="0 0 12 12" aria-hidden="true"><path d="M3 0h6a1 1 0 0 1 1 1v10a1 1 0 0 1-1 1H3a1 1 0 0 1-1-1V1a1 1 0 0 1 1-1zm0.5 1.5v8h5v-8z"/></svg>
          425.318.4762
        </li>
        <li>
          <svg class="contact-icon" viewBox="0 0 12 12" aria-hidden="true"><path d="M0 2h12v8H0zM0.8 2.6 6 6.6l5.2-4z" fill-rule="evenodd"/></svg>
          rbrantley@brantleyag-example.com
        </li>
        <li>
          <svg class="contact-icon" viewBox="0 0 12 12" aria-hidden="true"><circle cx="6" cy="6" r="6"/><path d="M0 6h12M6 0c-2.5 3-2.5 9 0 12M6 0c2.5 3 2.5 9 0 12" stroke="#fff" stroke-width=".9" fill="none"/></svg>
          www.brantleyag-example.com
        </li>
      </ul>
    </div>
  </section>
</main>
</body>
</html>
```